Hockey Sponsorship Proposal

We are looking for a sponsorship proposal design for an apparel company to supply our hockey camps with jerseys and apparel. We want to use lots of visuals so potential business partners can see the exposure and publicity their company could get by working with us. We would like the primary colors to be red, black and white. We have attached a bunch of images but not all need to be used. We would like to see a mix of images with adult players and youth players where appropriate. Although I have provided a rough outline for the information on the powerpoint the text and images can be displayed however you would like.

Here is a link to some proposals to give you an idea of what we are looking for
https://www.quillrack.co.uk/pin/512604837219056471/

Target Market(s)

Athletic Apparel Companies

Industry/Entity Type

It Company

Requirements
Must have
• Please note this should be suitable for web as the proposal will be emailed. This is NOT for print.
Nice to have
• I would like the first page to have a full image as the backdrop with the text over top if possible.

```html
<!DOCTYPE html>
<html lang="en">
<head>
<meta charset="utf-8">
<title>Northvale Hockey – Request for Proposal</title>
<link rel="stylesheet" href="https://fonts.googleapis.com/css2?family=Barlow:wght@400;700&display=swap">
<style>
  :root {
    --backdrop: #e9e6e1;
    --charcoal: #2b2b2d;
    --ink: #141414;
    --white: #f7f7f7;
    --red: #d8222b;
    --maroon: #7c1e2c;
    --maroon-deep: #5e1620;
    --photo-red: #8c2a2a;
    --photo-navy: #2a3350;
  }
  html, body {
    margin: 0;
    width: 1200px;
    height: 880px;
    overflow: hidden;
    background: var(--backdrop);
  }
  .cover {
    position: absolute;
    left: 50px;
    top: 60px;
    width: 1100px;
    height: 760px;
    box-shadow: 0 12px 30px rgba(0,0,0,.25);
    overflow: hidden;
    font-family: "Barlow", sans-serif;
  }
  .cover-art {
    position: absolute;
    inset: 0;
    display: block;
  }
  .brand {
    position: absolute;
    left: 62px;
    top: 118px;
    display: flex;
    align-items: center;
    gap: 14px;
  }
  .brand-mark {
    width: 22px;
    height: 22px;
    background: var(--red);
  }
  .brand-name {
    color: var(--white);
    font-weight: 700;
    font-size: 30px;
    letter-spacing: 2px;
    text-transform: uppercase;
  }
  .title-block {
    position: absolute;
    left: 70px;
    top: 616px;
    color: var(--white);
  }
  .title-kicker {
    margin: 0;
    font-weight: 400;
    font-size: 30px;
    letter-spacing: 1px;
  }
  .title-main {
    margin: 4px 0 0;
    font-weight: 700;
    font-size: 30px;
    letter-spacing: 1.5px;
  }
</style>
</head>
<body>
  <main class="cover">
    <svg class="cover-art" viewBox="0 0 1100 760" xmlns="http://www.w3.org/2000/svg">
      <defs>
        <linearGradient id="photoTone" x1="0" y1="0" x2="1" y2="0">
          <stop offset="0" stop-color="var(--photo-red)"/>
          <stop offset="0.55" stop-color="#6a2630"/>
          <stop offset="1" stop-color="var(--photo-navy)"/>
        </linearGradient>
      </defs>
      <rect class="field-dark" width="1100" height="760" fill="var(--charcoal)"/>
      <g role="img" aria-label="Photograph of two hockey players in helmets and team jerseys">
        <path class="player-photo" d="M40 330 Q180 270 330 320 Q470 250 620 300 L560 760 L40 760 Z" fill="url(#photoTone)" opacity="0.9"/>
      </g>
      <polygon class="panel-white" points="770,0 1100,0 1100,760 470,760" fill="var(--white)"/>
      <polygon class="stripe-maroon" points="690,0 770,0 500,690 420,690" fill="var(--maroon)" opacity="0.75"/>
      <polygon class="stripe-red" points="990,230 1050,230 870,690 810,690" fill="var(--red)"/>
      <rect class="band" x="0" y="590" width="1100" height="110" fill="var(--maroon)" opacity="0.92"/>
      <polygon class="block-black" points="890,545 1075,545 1020,640 835,640" fill="var(--ink)"/>
      <polygon class="block-black-low" points="930,760 1100,700 1100,760" fill="var(--ink)"/>
      <rect class="band-edge" x="0" y="700" width="470" height="6" fill="var(--maroon-deep)"/>
    </svg>

    <div class="brand">
      <span class="brand-mark"></span>
      <span class="brand-name">Northvale Hockey</span>
    </div>

    <div class="title-block">
      <p class="title-kicker">Uniform and Apparel Partnership Opportunity</p>
      <h1 class="title-main">REQUEST FOR PROPOSAL</h1>
    </div>
  </main>
</body>
</html>
```